The Quiet Harbor

I have a faux cover I will attach & want you to follow & enhance what I've created. Just an FYI, the book will be posted on brindlo & I'm working with Marrow Lane Publishing.
What you need to know:
The dimensions: 6" x 9" (15.24 x 22.86 cm)
Background color: Black
I did not capture the color of the font, so want you to get a similar gold color.
Font for title, subtitle & author name: Goudy Old Style
Font for "20th Anniversary Edition": Kunstler Script
I have thoughts of shaping the photo in an oval shape -- possibly shade out the edges?

Target Market(s)

All ages: anyone who has encountered issues with doctors, hospitals, and especially those who have struggled with cancer treatment.

Requirements
Nice to have
• Adding below another PDF, showing vintage lines that I would like to see used. Just added some text I will add to the back cover. I am waiting on one more review, which I will add. Attaching that below.

```html
<!DOCTYPE html>
<html lang="en">
<head>
<meta charset="utf-8">
<title>The Quiet Harbor – Cover</title>
<link rel="stylesheet" href="https://fonts.googleapis.com/css2?family=Sorts+Mill+Goudy:ital@0;1&family=Pinyon+Script&display=swap">
<style>
  :root {
    --page-bg: #d4d4d4;
    --cover-black: #000000;
    --gold-light: #f1cf8c;
    --gold-mid: #d9a452;
    --gold-deep: #c4861f;
    --ribbon-pink: #e0457e;
    --photo-light: #d8d8d8;
    --photo-dark: #3a3a3a;
  }
  * { margin: 0; padding: 0; box-sizing: border-box; }
  html, body {
    width: 1200px;
    height: 1200px;
    overflow: hidden;
    background: var(--page-bg);
  }
  .cover {
    position: absolute;
    left: 276px;
    top: 114px;
    width: 647px;
    height: 971px;
    background: var(--cover-black);
    overflow: hidden;
  }
  .gold-text {
    background: linear-gradient(90deg, var(--gold-light) 0%, var(--gold-mid) 45%, var(--gold-deep) 75%, var(--gold-mid) 100%);
    -webkit-background-clip: text;
    background-clip: text;
    color: transparent;
  }
  .cover__title {
    position: absolute;
    top: 88px;
    left: 0;
    width: 100%;
    text-align: center;
    font-family: "Sorts Mill Goudy", Georgia, serif;
    font-weight: 400;
    font-size: 50px;
    line-height: 1;
    letter-spacing: 0;
    white-space: nowrap;
  }
  .cover__subtitle {
    position: absolute;
    top: 174px;
    left: 0;
    width: 100%;
    text-align: center;
    font-family: "Sorts Mill Goudy", Georgia, serif;
    font-style: italic;
    font-size: 26px;
    line-height: 36px;
    white-space: nowrap;
  }
  .cover__edition {
    position: absolute;
    top: 280px;
    left: 0;
    width: 100%;
    text-align: center;
    font-family: "Pinyon Script", cursive;
    font-size: 35px;
    line-height: 1;
    white-space: nowrap;
  }
  .cover__frame {
    position: absolute;
    left: 67px;
    top: 362px;
    width: 514px;
    height: 375px;
    padding: 7px;
    background: linear-gradient(90deg, var(--gold-light), var(--gold-mid) 40%, var(--gold-deep) 65%, var(--gold-light));
  }
  .cover__photo {
    width: 100%;
    height: 100%;
    background: radial-gradient(ellipse at 50% 45%, var(--photo-dark) 0%, #6e6e6e 45%, var(--photo-light) 100%);
  }
  .cover__ribbon {
    position: absolute;
    left: 311px;
    top: 786px;
    width: 25px;
    height: 38px;
  }
  .cover__author {
    position: absolute;
    top: 853px;
    left: 0;
    width: 100%;
    text-align: center;
    font-family: "Sorts Mill Goudy", Georgia, serif;
    font-size: 27px;
    line-height: 1;
    white-space: nowrap;
  }
</style>
</head>
<body>
  <main class="cover">
    <h1 class="cover__title gold-text">THE QUIET HARBOR</h1>
    <p class="cover__subtitle gold-text">A tale of lifelong damage from terminal cancer<br>“treatment” &amp; inhumane doctors</p>
    <p class="cover__edition gold-text">20th Anniversary Edition</p>
    <div class="cover__frame">
      <div class="cover__photo" role="img" aria-label="Black and white photograph of the author seated in her living room"></div>
    </div>
    <svg class="cover__ribbon" viewBox="0 0 25 38" aria-hidden="true">
      <path d="M12.5 3 C6 3 5 10 8 15 L2 35 L6 37 L12.5 22 L19 37 L23 35 L17 15 C20 10 19 3 12.5 3 Z M12.5 7 C16 7 16 11 14.5 14 L12.5 18 L10.5 14 C9 11 9 7 12.5 7 Z" fill="var(--ribbon-pink)" fill-rule="evenodd"/>
    </svg>
    <p class="cover__author gold-text">Nora Whitfield</p>
  </main>
</body>
</html>
```